Business Card - Cooperate

Business Card for Larkfield Management Consulting

Target Market(s)

Corparte - b2B

Industry/Entity Type

Management Consulting - Professional Services

Contact Information for Business Card

Company Name , Slogan , Dummy Address,

Requirements
Must have
• Reach your Full Potential

```html
<!DOCTYPE html>
<html lang="en">
<head>
<meta charset="UTF-8">
<title>Larkfield Management Consulting – Business Card</title>
<link rel="stylesheet" href="https://fonts.googleapis.com/css2?family=Montserrat:wght@400;500;600&display=swap">
<style>
  :root {
    --backdrop: #1f2a22;
    --card: #efefef;
    --card-edge: #e4e4e4;
    --navy: #2f3aa0;
    --blue: #3567c8;
    --green: #3fd46a;
    --teal: #1fb89a;
    --blob: #dcdde3;
  }
  * { margin: 0; padding: 0; box-sizing: border-box; }
  html, body {
    width: 1200px; height: 800px; overflow: hidden;
    background: var(--backdrop);
    font-family: "Montserrat", sans-serif;
  }
  .canvas {
    position: relative; width: 1200px; height: 800px;
    display: flex; align-items: center; justify-content: center; gap: 40px;
  }
  .card {
    position: relative; width: 520px; height: 300px;
    background: linear-gradient(135deg, #f6f6f6, var(--card-edge));
    border-radius: 22px; overflow: hidden;
  }
  .corner-blob {
    position: absolute; left: -40px; top: -50px;
    width: 150px; height: 130px; border-radius: 50%;
    background: var(--blob); opacity: .55;
  }
  /* Back: contact details */
  .contact-name {
    position: absolute; left: 36px; top: 48px;
    font-size: 34px; font-weight: 400; color: var(--navy); letter-spacing: .5px;
  }
  .contact-role {
    position: absolute; left: 38px; top: 94px;
    font-size: 12px; color: var(--green); letter-spacing: 1.2px;
  }
  .contact-list {
    position: absolute; left: 38px; top: 128px;
    list-style: none; font-size: 14px; line-height: 21px; color: var(--navy);
  }
  .contact-list .label { color: var(--green); font-weight: 600; margin-right: 4px; }
  .contact-address {
    position: absolute; left: 300px; bottom: 32px;
    font-size: 14px; line-height: 20px; color: var(--navy);
  }
  /* Front: brand */
  .brand {
    position: absolute; inset: 0;
    display: flex; flex-direction: column; align-items: center; justify-content: center;
  }
  .brand-row { display: flex; align-items: center; gap: 16px; }
  .brand-dot { width: 40px; height: 40px; border-radius: 50%; background: var(--blue); }
  .brand-name { font-size: 58px; font-weight: 500; color: var(--blue); letter-spacing: 1px; }
  .brand-tagline {
    margin-top: 8px; font-size: 13px; font-weight: 600;
    color: var(--teal); letter-spacing: 3px;
  }
</style>
</head>
<body>
<main class="canvas">
  <section class="card card--back">
    <div class="corner-blob"></div>
    <h1 class="contact-name">Daniel Hart</h1>
    <p class="contact-role">SALES &amp; PROPERTY MANAGEMENT</p>
    <ul class="contact-list">
      <li><span class="label">M:</span>040 555 0127</li>
      <li><span class="label">E:</span>daniel@larkfield.net.au</li>
      <li><span class="label">W:</span>larkfield.net.au</li>
    </ul>
    <address class="contact-address" style="font-style:normal">2207 Alder Way,<br>Ridgeview, CA90000</address>
  </section>

  <section class="card card--front">
    <div class="corner-blob"></div>
    <div class="brand">
      <div class="brand-row">
        <span class="brand-dot"></span>
        <span class="brand-name">Larkfield</span>
      </div>
      <p class="brand-tagline">REACH YOUR FULL POTENTIAL</p>
    </div>
  </section>
</main>
</body>
</html>
```